Varnel Group Business Card design with current logo

hello all , we have abranded logo which i will attach but we need a card double sided designed . one side is easy as its the logo but the other side we want clean and modern. The info needed will be the same text as the card sample attached. no pictures of us though just clean and professinal pls. Logo can be incorporated on the text side to for recognition. Colors are Black , white , red and grey... ideal card would be matt finish high end stock. or a black card so white text ... Sorry i have uploaded al the files i got when I had the logo designed on here.. Oh forgot want to say pls add in the card details EST 1983 and over 40yrs combined experiance
Updates

Hello everyone , I'm really sorry we haven't been able to make a final decision.. There is at least 3 cards that all have there positives over the other two... We will decide by tonight.

Target Market(s)

20-70 wide range but people with money and a education.

Industry/Entity Type

Real Estate Agent

Contact Information for Business Card

One side the Logo choose from the different color logos, black being the one we like most, other side is the details. Clean professional looking fonts. EST 1983 , over 40yrs experiance. Website email and both names and PH# as per the sample card attached

Font styles to use
Other font styles liked:
• Fonts:Code Bold,Code Light, Lucida Fax.

Colors
1b1b1b
757575
c9c9c9
e8e8e8
ffffff
e9e9e9

Requirements
Must have
• Logo and contact info

```html
<!DOCTYPE html>
<html lang="en">
<head>
<meta charset="utf-8">
<title>Varnel Real Estate – Business Cards</title>
<link rel="stylesheet" href="https://fonts.googleapis.com/css2?family=Cinzel:wght@400&family=Noto+Serif:wght@400&display=swap">
<style>
  :root {
    --page: #ffffff;
    --page-edge: #8a8a8a;
    --black-card: #1b1b1b;
    --grey-card: #dcdcdc;
    --red-card: #bb1a1c;
    --ink-light: #ffffff;
    --ink-dark: #1b1b1b;
    --ink-on-red: #2b0d0d;
    --accent-red: #c8161b;
  }
  * { margin: 0; padding: 0; box-sizing: border-box; }
  html, body { width: 1200px; height: 1128px; overflow: hidden; background: var(--page); }
  .sheet {
    position: relative; width: 1200px; height: 1128px;
    border: 1px solid var(--page-edge);
  }
  .card {
    position: absolute; width: 521px; height: 298px; overflow: hidden;
    font-family: "Noto Serif", Georgia, serif;
    font-weight: 400;
    color: var(--ink);
    background: var(--bg);
  }
  .theme-black { --bg: var(--black-card); --ink: var(--ink-light); --rule: rgba(255,255,255,.55); --mark: var(--accent-red); }
  .theme-grey  { --bg: var(--grey-card);  --ink: var(--ink-dark);  --rule: rgba(0,0,0,.45); --mark: var(--accent-red); }
  .theme-red   { --bg: var(--red-card);   --ink: var(--ink-on-red); --rule: rgba(0,0,0,.5); --mark: #d9d9d9; }

  .front { left: 50px; }
  .back  { left: 637px; }
  .row-1 { top: 50px; }
  .row-2 { top: 412px; }
  .row-3 { top: 781px; }

  /* Front: wordmark */
  .wordmark {
    position: absolute; left: 0; right: 0; top: 104px;
    text-align: center;
    font-family: "Cinzel", "Times New Roman", serif;
    font-weight: 400;
    color: var(--ink);
  }
  .wordmark-name { display: block; font-size: 56px; line-height: 66px; letter-spacing: 1px; }
  .wordmark-sub  { display: block; font-size: 27px; line-height: 34px; letter-spacing: 1px; }

  /* Back: brokerage name */
  .brokerage {
    position: absolute; right: 23px; top: 23px;
    display: flex; align-items: center; gap: 5px;
    color: var(--ink);
  }
  .brokerage-square { width: 9px; height: 9px; background: var(--mark); }
  .brokerage-text { font-size: 11px; line-height: 12px; text-align: left; }
  .brokerage-tag { display: block; font-size: 5px; line-height: 7px; letter-spacing: .2px; }

  .names {
    position: absolute; left: 0; right: 0; top: 88px;
    text-align: center; font-size: 26px; line-height: 35px; letter-spacing: .3px;
    font-weight: 400;
  }
  .names-rule {
    display: block; width: 172px; height: 1px; margin: 0 auto;
    background: var(--rule);
  }

  .established {
    position: absolute; left: 0; right: 0; top: 204px;
    text-align: center; font-size: 14.8px; line-height: 20px; letter-spacing: -.1px;
  }
  .contact-rule {
    position: absolute; left: 22px; right: 22px; top: 226px; height: 1px;
    background: linear-gradient(90deg, transparent, var(--rule) 20%, var(--rule) 80%, transparent);
  }
  .contact {
    position: absolute; left: 0; right: 0; top: 229px;
    text-align: center; font-size: 14.8px; line-height: 17.6px; letter-spacing: -.1px;
    font-style: normal; white-space: nowrap;
  }
</style>
</head>
<body>
<main class="sheet">

  <!-- Black set -->
  <section class="card front theme-black row-1">
    <h1 class="wordmark"><span class="wordmark-name">Varnel</span><span class="wordmark-sub">Real Estate</span></h1>
  </section>
  <section class="card back theme-black row-1">
    <div class="brokerage"><span class="brokerage-square"></span><span class="brokerage-text">Harbourline Realty<span class="brokerage-tag">LOCALLY OWNED AND OPERATED</span></span></div>
    <h2 class="names">DALE VARNEL<span class="names-rule"></span>MORGAN VARNEL</h2>
    <p class="established">EST 1983, OVER 40 YEARS EXPERIENCE</p>
    <span class="contact-rule"></span>
    <address class="contact">Phone: 250-555-0142 &nbsp;/&nbsp; Fax: 250-555-0187<br>Email: info@varnelrealestate.com / &nbsp;Web: www.varnelrealestate.com<br>Harbourline Realty, 210 - 3875 Alder Crest Road Kelmore BC K4T 2R9</address>
  </section>

  <!-- Grey set -->
  <section class="card front theme-grey row-2">
    <h1 class="wordmark"><span class="wordmark-name">Varnel</span><span class="wordmark-sub">Real Estate</span></h1>
  </section>
  <section class="card back theme-grey row-2">
    <div class="brokerage"><span class="brokerage-square"></span><span class="brokerage-text">Harbourline Realty<span class="brokerage-tag">LOCALLY OWNED AND OPERATED</span></span></div>
    <h2 class="names">DALE VARNEL<span class="names-rule"></span>MORGAN VARNEL</h2>
    <p class="established">EST 1983, OVER 40 YEARS EXPERIENCE</p>
    <span class="contact-rule"></span>
    <address class="contact">Phone: 250-555-0142 &nbsp;/&nbsp; Fax: 250-555-0187<br>Email: info@varnelrealestate.com / &nbsp;Web: www.varnelrealestate.com<br>Harbourline Realty, 210 - 3875 Alder Crest Road Kelmore BC K4T 2R9</address>
  </section>

  <!-- Red set -->
  <section class="card front theme-red row-3">
    <h1 class="wordmark"><span class="wordmark-name">Varnel</span><span class="wordmark-sub">Real Estate</span></h1>
  </section>
  <section class="card back theme-red row-3">
    <div class="brokerage"><span class="brokerage-square"></span><span class="brokerage-text">Harbourline Realty<span class="brokerage-tag">LOCALLY OWNED AND OPERATED</span></span></div>
    <h2 class="names">DALE VARNEL<span class="names-rule"></span>MORGAN VARNEL</h2>
    <p class="established">EST 1983, OVER 40 YEARS EXPERIENCE</p>
    <span class="contact-rule"></span>
    <address class="contact">Phone: 250-555-0142 &nbsp;/&nbsp; Fax: 250-555-0187<br>Email: info@varnelrealestate.com / &nbsp;Web: www.varnelrealestate.com<br>Harbourline Realty, 210 - 3875 Alder Crest Road Kelmore BC K4T 2R9</address>
  </section>

</main>
</body>
</html>
```